Save the date for wedding

A save the date for our wedding. We're looking for a simple and sleek invite. I would prefer not alot of calligraphy. Minimalism is good. The basic info to include is as follows:
Names: Mavis and Colin
Date: June 9th
Where: Ottawa, Ontario
In small print please include that there will be a reception in Edmonton AB September 1st for those who cannot make it to Ottawa.
Please see the attached file for a style idea. Doesn’t have to be exactly like that, but something like that.
Wedding

```html
<!DOCTYPE html>
<html lang="en">
<head>
<meta charset="utf-8">
<title>Save the Date – Colin and Mavis</title>
<link rel="stylesheet" href="https://fonts.googleapis.com/css2?family=Caveat+Brush&family=Dancing+Script:wght@500&family=Jost:wght@300;400;600&display=swap">
<style>
  :root {
    --paper: #fffdfd;
    --ink: #1f1f1f;
    --names: #a8896b;
    --rose: #f19db4;
    --leaf: #5f8a86;
    --leaf-light: #9fbf7a;
    --leaf-blue: #4ea3c4;
  }
  * { margin: 0; padding: 0; box-sizing: border-box; }
  html, body {
    width: 849px;
    height: 1200px;
    overflow: hidden;
    background: var(--paper);
  }
  .card {
    position: relative;
    width: 849px;
    height: 1200px;
    background: var(--paper);
    font-family: "Jost", sans-serif;
    color: var(--ink);
    text-align: center;
  }
  .floral-crown {
    position: absolute;
    left: 100px;
    top: 52px;
    width: 690px;
    height: 310px;
    border-radius: 50% 50% 45% 45% / 40% 40% 60% 60%;
    background:
      radial-gradient(ellipse 36% 42% at 50% 42%, var(--rose) 0%, rgba(241,157,180,0.5) 60%, transparent 100%),
      linear-gradient(100deg, var(--leaf) 0%, var(--leaf-light) 45%, var(--leaf-light) 55%, var(--leaf-blue) 100%);
    opacity: 0.85;
  }
  .headline {
    position: absolute;
    left: 0;
    top: 0;
    width: 100%;
    font-family: "Dancing Script", cursive;
    font-weight: 500;
    color: var(--rose);
  }
  .headline span {
    position: absolute;
    left: 0;
    width: 100%;
    line-height: 1;
  }
  .headline .word-save { top: 350px; font-size: 150px; }
  .headline .word-the  { top: 482px; font-size: 78px; }
  .headline .word-date { top: 530px; font-size: 150px; }
  .couple-names {
    position: absolute;
    left: 0;
    top: 688px;
    width: 100%;
    font-family: "Caveat Brush", cursive;
    font-weight: 400;
    font-size: 88px;
    line-height: 1;
    color: var(--names);
    letter-spacing: -1px;
  }
  .couple-names .conjunction {
    font-size: 34px;
    margin: 0 22px;
    vertical-align: 14px;
  }
  .announcement {
    position: absolute;
    left: 0;
    top: 798px;
    width: 100%;
    font-size: 21px;
    font-weight: 400;
    line-height: 1.4;
  }
  .leaf-sprig {
    position: absolute;
    left: 340px;
    top: 872px;
    width: 164px;
    height: 118px;
    border-radius: 60% 40% 60% 40%;
    background: linear-gradient(160deg, var(--leaf-blue) 0%, var(--leaf) 60%, #5b5a48 100%);
    opacity: 0.75;
  }
  .event-date,
  .event-place {
    position: absolute;
    left: 0;
    width: 100%;
    font-size: 46px;
    font-weight: 400;
    line-height: 1;
  }
  .event-date { top: 1004px; }
  .event-place { top: 1056px; }
  .reception-note {
    position: absolute;
    left: 0;
    top: 1110px;
    width: 100%;
    font-size: 23px;
    font-weight: 400;
    line-height: 1.3;
  }
  .reception-note strong { font-weight: 600; }
</style>
</head>
<body>
  <main class="card">
    <div class="floral-crown" role="img" aria-label="Watercolour arrangement of three pink roses with green and blue leaves and berry sprigs"></div>

    <h1 class="headline">
      <span class="word-save">Save</span>
      <span class="word-the">the</span>
      <span class="word-date">Date</span>
    </h1>

    <h2 class="couple-names">Colin<span class="conjunction">and</span>Mavis</h2>

    <p class="announcement">We are getting<br>married</p>

    <div class="leaf-sprig" role="img" aria-label="Small watercolour sprig of blue-green leaves"></div>

    <p class="event-date">June 9th</p>
    <p class="event-place">Ottawa, Ontario</p>

    <p class="reception-note">There will be a reception in <strong>Edmonton AB</strong> September 1st<br>for those who cannot make it to Ottawa.</p>
  </main>
</body>
</html>
```